4K Business Card Design

We need a business card that emphasizes consulting services worldwide. The name of the company is KKKK Consulting Group. We provide consulting services across several industries including but not limited to commodities, telecom, manufacturing, logistics, marketing and operations. We would like to see a creative design that emphasizes the global aspect, including Latin America and US markets, as well the bilingual nature of the service offerings.

The contact information section should include icons to represent the following data:
1) Name, Title and Company Name
2) Mobile Number
3) Skype ID
4) Email
5) Web Page
6) Location

We would like to see a card that emphasizes the worldwide concept. The back of the card should be simple, including only the logo (or a portion of the logo) and the slogan.

We would also like to see business cards in a booklet format. The colors to be used should be the same combination of colors used in the logos attached to this brief.

The logo design and some business card examples from Artful Herd are attached for reference on style and look.

Target Market(s)

International business executives, 45-65 years of age, bilingual

Industry/Entity Type

Marketing

Colors
0792cd
34a7d8
85cae6
ffffff
cee9f5
ecf7fb

Requirements
Must have
• Please follow colors in logo attached.

2) Mobile Number
3) Skype ID
4) Email
5) Web Page
6) Location
Nice to have
• Global concept, consulting profile, diverse industry focus
Should not have
• No black color

```html
<!DOCTYPE html>
<html lang="en">
<head>
<meta charset="utf-8">
<title>KKKK Consulting Group – Business Card</title>
<link rel="stylesheet" href="https://fonts.googleapis.com/css2?family=Tinos:ital,wght@0,400;1,400&display=swap">
<style>
  :root {
    --stage: #2b2927;
    --front-bg: #eef8fc;
    --ink-blue: #1a96d0;
    --back-bg: #1192cf;
    --faint-front: #cfe3ee;
    --mid-front: #9cc8e0;
    --faint-back: #4ba8da;
    --mark-light: #d6ecf7;
    --white: #ffffff;
  }
  * { margin: 0; padding: 0; box-sizing: border-box; }
  html, body {
    width: 1200px; height: 1000px; overflow: hidden;
    background: var(--stage);
    font-family: "Tinos", "Times New Roman", serif;
  }
  .canvas { position: relative; width: 1200px; height: 1000px; }

  .card { position: absolute; width: 796px; height: 455px; overflow: hidden; }
  .card--front { left: 22px; top: 30px; background: var(--front-bg); }
  .card--back { left: 360px; top: 513px; background: var(--back-bg); }

  .brand-echo {
    position: absolute; white-space: nowrap; line-height: 1;
    font-weight: 400;
  }
  .card--front .brand-echo--large { right: -20px; top: 120px; font-size: 170px; color: var(--faint-front); }
  .card--front .brand-echo--small { right: 14px; top: 230px; font-size: 120px; color: var(--mid-front); }
  .card--back .brand-echo--large { right: -20px; top: 90px; font-size: 170px; color: var(--faint-back); }
  .card--back .brand-echo--small { right: 14px; top: 220px; font-size: 120px; color: var(--mark-light); }

  .holder { position: absolute; left: 27px; top: 28px; color: var(--ink-blue); }
  .holder__name { font-size: 44px; line-height: 1; }
  .holder__title { font-size: 22px; margin-top: 6px; }

  .contacts { position: absolute; left: 27px; top: 306px; color: var(--ink-blue); font-size: 22px; line-height: 24px; list-style: none; }

  .back-brand {
    position: absolute; left: 0; width: 424px; top: 24px;
    text-align: center; color: var(--mark-light); line-height: 1;
  }
  .back-brand__mark { font-size: 60px; }
  .back-brand__name { font-size: 46px; margin-top: 22px; }
  .back-brand__sub { font-size: 38px; margin-top: 6px; }

  .slogan {
    position: absolute; left: 22px; top: 378px;
    font-style: italic; font-size: 44px; color: var(--white);
  }
</style>
</head>
<body>
<main class="canvas">
  <section class="card card--front" aria-label="Card front">
    <div class="brand-echo brand-echo--large" aria-hidden="true">KKKK</div>
    <div class="brand-echo brand-echo--small" aria-hidden="true">KKKK</div>
    <header class="holder">
      <h1 class="holder__name" style="font-weight:400">John Doe</h1>
      <p class="holder__title">President &amp; CEO,KKKK Consulting Group</p>
    </header>
    <ul class="contacts">
      <li>Skype ID: JohnDoe</li>
      <li>Mobile: 123 456 7890</li>
      <li>Web: www.website.com</li>
      <li>Email: contact@wesite.com</li>
      <li>Address: 12345,Street DR,Suite 101,City,State,ZIP</li>
    </ul>
  </section>

  <section class="card card--back" aria-label="Card back">
    <div class="brand-echo brand-echo--large" aria-hidden="true">KKKK</div>
    <div class="brand-echo brand-echo--small" aria-hidden="true">KKKK</div>
    <div class="back-brand">
      <p class="back-brand__mark">KKKK</p>
      <p class="back-brand__name">Consulting</p>
      <p class="back-brand__sub">Group</p>
    </div>
    <p class="slogan">“Insert slogan here”</p>
  </section>
</main>
</body>
</html>
```